Accommodation business card design

We need a business card designed for our long-term accommodation business based in Australia. The business card must match the style of the attached letterhead and logo. The same contact details that are on the letterhead will also go on the card except that the card must list the contact details in the following order:phone, email, home address, ABN.

The card will be printed on .76mm white pvc plastic (same as credit cards), printed both sides and will be silver foil stamped on at least one side (preferably 2 sides) The design template is attached, but please go to www.zt.com.au for more specs.

The only other addition the card will be my name: Malcolm Darby

```html
<!DOCTYPE html>
<html lang="en">
<head>
<meta charset="utf-8">
<title>Summit Lodging – Business Card</title>
<link rel="stylesheet" href="https://fonts.googleapis.com/css2?family=Ubuntu:wght@400;500;700&display=swap">
<style>
  :root {
    --backdrop: #e6e4e2;
    --card: #ffffff;
    --plum: #8a1f4f;
    --berry: #a33a68;
    --terracotta: #b5604e;
    --terracotta-light: #c87b68;
    --ink: #4a4a4a;
    --shadow: rgba(0, 0, 0, 0.18);
  }
  * { box-sizing: border-box; margin: 0; padding: 0; }
  html, body {
    width: 1200px;
    height: 873px;
    overflow: hidden;
    background: var(--backdrop);
    font-family: "Ubuntu", sans-serif;
  }
  .sheet {
    position: relative;
    width: 1200px;
    height: 873px;
  }
  .card {
    position: absolute;
    top: 283px;
    width: 500px;
    height: 306px;
    background: var(--card);
    border-radius: 14px;
    overflow: hidden;
    box-shadow: 0 10px 28px var(--shadow);
  }
  .card--front { left: 70px; }
  .card--back { left: 630px; }
  .card__swoosh {
    position: absolute;
    inset: 0;
    width: 100%;
    height: 100%;
  }
  .brand {
    position: absolute;
    display: flex;
    align-items: center;
    gap: 12px;
  }
  .brand__mark {
    width: 40px;
    height: 40px;
    border-radius: 8px;
    background: var(--plum);
    flex: none;
  }
  .brand__name {
    font-weight: 700;
    font-size: 28px;
    line-height: 0.95;
    letter-spacing: 1px;
    text-transform: uppercase;
    color: var(--plum);
  }
  .card--front .brand { top: 32px; left: 36px; }
  .card--back .brand { top: 62px; left: 110px; }
  .card--back .brand__mark { width: 54px; height: 54px; border-radius: 10px; }
  .card--back .brand__name { font-size: 34px; }
  .holder {
    position: absolute;
    top: 112px;
    left: 36px;
    font-weight: 700;
    font-size: 22px;
    color: var(--plum);
  }
  .contact {
    position: absolute;
    top: 152px;
    left: 240px;
    list-style: none;
    font-size: 11px;
    color: var(--ink);
  }
  .contact__item {
    display: flex;
    align-items: center;
    gap: 7px;
    margin-bottom: 5px;
    line-height: 1.25;
  }
  .contact__icon {
    width: 12px;
    height: 12px;
    flex: none;
  }
  .contact__item--abn { padding-left: 19px; color: var(--berry); }
</style>
</head>
<body>
<main class="sheet">

  <section class="card card--front" aria-label="Business card front">
    <svg class="card__swoosh" viewBox="0 0 500 306" preserveAspectRatio="none" aria-hidden="true">
      <path d="M0 168 C 110 232 260 280 420 306 L 0 306 Z" fill="var(--terracotta)"/>
      <path d="M0 196 C 110 252 230 290 330 306 L 0 306 Z" fill="var(--terracotta-light)" opacity="0.35"/>
      <path d="M180 306 C 320 282 430 258 500 212 L 500 236 C 430 276 340 298 270 306 Z" fill="var(--berry)"/>
    </svg>

    <div class="brand">
      <span class="brand__mark"></span>
      <span class="brand__name">Summit<br>Lodging</span>
    </div>

    <p class="holder">Malcolm Darby</p>

    <ul class="contact">
      <li class="contact__item">
        <svg class="contact__icon" viewBox="0 0 12 12" aria-hidden="true"><circle cx="6" cy="6" r="6" fill="var(--plum)"/><path d="M4 3 L5 3 L5.6 4.6 L4.9 5.2 Q5.6 6.5 6.8 7.1 L7.4 6.4 L9 7 L9 8 Q6 9 3.5 5.5 Q3.4 4 4 3 Z" fill="#fff"/></svg>
        0400 318 552
      </li>
      <li class="contact__item">
        <svg class="contact__icon" viewBox="0 0 12 12" aria-hidden="true"><circle cx="6" cy="6" r="6" fill="var(--plum)"/><rect x="3" y="4" width="6" height="4.2" fill="#fff"/><path d="M3 4 L6 6.4 L9 4" stroke="var(--plum)" stroke-width="0.7" fill="none"/></svg>
        malcolm.darby@mailbox.com
      </li>
      <li class="contact__item">
        <svg class="contact__icon" viewBox="0 0 12 12" aria-hidden="true"><circle cx="6" cy="6" r="6" fill="var(--plum)"/><path d="M6 2.6 A2.2 2.2 0 0 1 8.2 4.8 C8.2 6.4 6 9.2 6 9.2 C6 9.2 3.8 6.4 3.8 4.8 A2.2 2.2 0 0 1 6 2.6 Z" fill="#fff"/><circle cx="6" cy="4.8" r="0.8" fill="var(--plum)"/></svg>
        PO Box 1180, Ridgeview Mail Centre<br>QLD 4700
      </li>
      <li class="contact__item contact__item--abn">ABN 12 345 678 901</li>
    </ul>
  </section>

  <section class="card card--back" aria-label="Business card back">
    <svg class="card__swoosh" viewBox="0 0 500 306" preserveAspectRatio="none" aria-hidden="true">
      <path d="M0 0 L 70 0 C 40 90 110 220 260 306 L 0 306 Z" fill="var(--terracotta)"/>
      <path d="M0 0 L 40 0 C 20 90 70 210 180 306 L 0 306 Z" fill="var(--terracotta-light)" opacity="0.35"/>
      <path d="M96 140 C 150 220 260 270 500 290 L 500 306 L 470 306 C 270 296 150 240 96 140 Z" fill="var(--berry)"/>
    </svg>

    <div class="brand">
      <span class="brand__mark"></span>
      <span class="brand__name">Summit<br>Lodging</span>
    </div>
  </section>

</main>
</body>
</html>
```